Karriernet Banner Design (Profilbanner und Unternehmensbanner) (1584 x 396) (1128 x 191)
Zielgruppe
Ich bin Dienstleister und Unternehmensberater für technischen B2B Vertrieb.
Für meinen KarrierNet Account suche ich einen Banner für meine Profilseite und einen Banner für die Unternehmensseite). Meine Zielgruppe sind leitende Angestellte in Unternehmen. Das Design sollte entsprechend grafisch hochwertig, seriös gestaltet sein.
I am a service provider and management consultant for technical B2B sales.
For my KarrierNet account, I'm looking for a banner for my profile page and a banner for the company page). My target group are executives in companies. The design should have a correspondingly high-quality graphic design and be serious.
Aufgabenstellung
Wichtig ist die Berücksichtigung meines Logos (PNG im Anhang) und des Corporate Identity Farben (PDF Anhang und unten stehend). Stock Bilder oder Grafiken können/sollen gerne mit eingebunden werden. Wichtig ist hier der passende Gesamteindruck.
It is important to consider my logo (PNG in the attachment) and the corporate identity colors (PDF attachment and below). Stock images or graphics can/should be included. The right overall impression is important here.
HEX / HTML 002854
HEX / HTML 00b6e3
Bannergrößen / Banner sizes
Profilbanner (1584 x 396)
Unternehmensseitenbanner (1128 x 191)

```html
<!DOCTYPE html>
<html lang="de">
<head>
<meta charset="utf-8">
<title>Matthias Kernow Management &amp; Sales Consulting – Unternehmensseite</title>
<link href="https://fonts.googleapis.com/css2?family=Titillium+Web:wght@300;400;600;700&family=Source+Sans+3:wght@400;600&display=swap" rel="stylesheet">
<style>
  :root {
    --navy: #002854;
    --cyan: #00b6e3;
    --blue-deep: #0a3f86;
    --blue-mid: #0b5cbf;
    --blue-bright: #1a74d4;
    --logo-bg: #1a2a48;
    --photo-dark: #0c1a33;
    --photo-mid: #1b3f7a;
    --text-dark: #1d1d1d;
    --text-mid: #444;
    --text-soft: #666;
    --button-blue: #0a66c2;
    --white: #ffffff;
  }
  * { margin: 0; padding: 0; box-sizing: border-box; }
  html, body { width: 1200px; height: 656px; overflow: hidden; background: var(--white); }
  .page { position: relative; width: 1200px; height: 656px; font-family: "Source Sans 3", sans-serif; }

  .banner { position: absolute; left: 0; top: 0; width: 1200px; height: 303px; overflow: hidden;
    background: linear-gradient(100deg, var(--blue-deep) 0%, var(--blue-mid) 45%, var(--blue-bright) 70%); }
  .banner-shade { position: absolute; inset: 0;
    background: linear-gradient(160deg, rgba(0,20,60,0.55) 0%, rgba(0,20,60,0) 40%); }
  .banner-photo { position: absolute; left: 0; top: 0; width: 1200px; height: 303px;
    clip-path: polygon(679px 0, 1200px 0, 1200px 303px, 521px 303px);
    background: radial-gradient(ellipse at 68% 45%, #6f7c8f 0%, #2a3650 25%, var(--photo-dark) 55%),
                linear-gradient(90deg, var(--photo-mid), var(--photo-dark)); }
  .headline { position: absolute; color: var(--white); font-family: "Titillium Web", sans-serif;
    line-height: 1; letter-spacing: 0.5px; }
  .headline .light { font-weight: 300; font-size: 31px; }
  .headline .bold { font-weight: 700; font-size: 40px; }
  .headline-1 { left: 155px; top: 58px; }
  .headline-2 { left: 194px; top: 110px; }
  .contact { position: absolute; top: 263px; display: flex; align-items: center; gap: 7px;
    color: var(--white); font-family: "Titillium Web", sans-serif; font-weight: 600; font-size: 14px; }
  .contact-phone { left: 232px; }
  .contact-web { left: 400px; }

  .brand-tile { position: absolute; left: 39px; top: 213px; width: 167px; height: 164px;
    background: var(--logo-bg); border: 3px solid var(--white); display: flex; align-items: center; justify-content: center; }
  .brand-name { color: var(--cyan); font-family: "Titillium Web", sans-serif; font-weight: 600; font-size: 28px; }

  .company-name { position: absolute; left: 35px; top: 398px; font-size: 37px; font-weight: 600; color: var(--text-dark); letter-spacing: 0.2px; }
  .tagline { position: absolute; left: 35px; top: 447px; font-size: 20px; color: var(--text-mid); }
  .meta { position: absolute; left: 34px; top: 481px; font-size: 17px; color: var(--text-soft); }
  .staff { position: absolute; left: 35px; top: 526px; font-size: 19px; font-weight: 600; color: var(--text-soft); }

  .actions { position: absolute; top: 583px; left: 35px; display: flex; gap: 13px; }
  .btn { height: 49px; border-radius: 25px; display: flex; align-items: center; justify-content: center;
    gap: 8px; font-size: 22px; font-weight: 600; }
  .btn-follow { width: 210px; background: var(--button-blue); color: var(--white); }
  .btn-website { width: 292px; border: 2px solid var(--button-blue); color: var(--button-blue); }
  .btn-more { width: 110px; border: 2px solid #666; color: #555; font-weight: 400; }
</style>
</head>
<body>
<div class="page">
  <section class="banner">
    <div class="banner-shade"></div>
    <div class="banner-photo" role="img" aria-label="Foto eines Automotors mit Riementrieb vor Carbonmuster"></div>
    <p class="headline headline-1"><span class="light">VOLLE </span><span class="bold">POWER</span></p>
    <p class="headline headline-2"><span class="light">FÜR IHR </span><span class="bold">BUSINESS</span><span class="light">.</span></p>
    <div class="contact contact-phone">
      <svg width="24" height="24" viewBox="0 0 24 24" fill="none" stroke="#fff" stroke-width="1.6" aria-hidden="true">
        <path d="M5 3h4l2 5-2.5 1.5a11 11 0 0 0 6 6L16 13l5 2v4a2 2 0 0 1-2 2A17 17 0 0 1 3 5a2 2 0 0 1 2-2z"/>
      </svg>
      <span>0987 | 654 321 0</span>
    </div>
    <div class="contact contact-web">
      <svg width="24" height="24" viewBox="0 0 24 24" fill="none" stroke="#fff" stroke-width="1.5" aria-hidden="true">
        <circle cx="12" cy="12" r="10"/><ellipse cx="12" cy="12" rx="4.5" ry="10"/>
        <path d="M2 12h20M4 6.5h16M4 17.5h16"/>
      </svg>
      <span>MATTHIASKERNOW.DE</span>
    </div>
  </section>

  <div class="brand-tile"><span class="brand-name">Kernow</span></div>

  <h1 class="company-name">Matthias Kernow Management &amp; Sales Consulting GmbH</h1>
  <p class="tagline">B2B Sales Consulting</p>
  <p class="meta">Business Consulting und Unternehmensdienstleistungen · Bad Lindenau, North Rhine-Westphalia · 1 Follower</p>
  <p class="staff">1 Mitarbeiter:in auf KarrierNet ansehen</p>

  <div class="actions">
    <div class="btn btn-follow">+ Folgen</div>
    <div class="btn btn-website">Website besuchen
      <svg width="24" height="24" viewBox="0 0 24 24" fill="none" stroke="#0a66c2" stroke-width="2.4" aria-hidden="true">
        <path d="M10 5H5v14h14v-5"/><path d="M13 4h7v7M20 4l-9 9"/>
      </svg>
    </div>
    <div class="btn btn-more">Mehr</div>
  </div>
</div>
</body>
</html>
```